Bright Valley Centre - is state of the art audiology clinic and needs a business card design

the card should be oriented in 'portrait' mode and have a clinic logo. The card should be double sided, with logo on the front and my details on the other side of the card

We would also like to use a tagline of 'Experts in Hearing Care'

```html
<!DOCTYPE html>
<html lang="en">
<head>
<meta charset="utf-8">
<title>Bright Valley Centre – Business Card</title>
<link href="https://fonts.googleapis.com/css2?family=Questrial&family=Open+Sans:ital,wght@0,400;0,700;1,400&display=swap" rel="stylesheet">
<style>
  :root {
    --page-bg: #e9eaec;
    --white: #ffffff;
    --ink-grey: #6d7378;
    --blue-deep: #2f8ff0;
    --blue-mid: #4aa6f5;
    --blue-light: #7cc3fb;
    --cyan-band: #86e3fb;
    --cyan-line: #a9eafc;
    --address-blue: #2f8ff0;
    --card-border: #3a3a3a;
  }
  * { box-sizing: border-box; margin: 0; padding: 0; }
  html, body { width: 1200px; height: 702px; overflow: hidden; }
  body {
    background: var(--page-bg);
    font-family: "Questrial", "Century Gothic", sans-serif;
    position: relative;
  }
  .card {
    position: absolute;
    top: 71px;
    width: 312px;
    height: 560px;
    border: 1px solid var(--card-border);
    overflow: hidden;
    background: var(--white);
  }
  .card--front { left: 258px; }
  .card--back { left: 630px; }

  .brand {
    position: absolute;
    left: 0; right: 0;
    display: flex;
    align-items: center;
    justify-content: center;
  }
  .brand__dot { border-radius: 50%; flex: none; }
  .brand__name {
    text-transform: uppercase;
    line-height: 1.08;
  }

  /* Front side */
  .card--front {
    background: radial-gradient(ellipse at 50% 42%, var(--blue-light) 0%, var(--blue-mid) 42%, var(--blue-deep) 100%);
  }
  .card--front .brand { top: 186px; gap: 20px; }
  .card--front .brand__dot { width: 44px; height: 44px; background: var(--white); }
  .card--front .brand__name { font-size: 26px; color: var(--white); letter-spacing: 1.5px; }
  .tagline-band {
    position: absolute;
    left: 0; right: 0; bottom: 0;
    height: 64px;
    background: var(--cyan-band);
    border-top: 4px solid var(--white);
    display: flex; align-items: center; justify-content: center;
    font-family: "Open Sans", sans-serif;
    font-style: italic;
    font-size: 19px;
    color: var(--white);
  }

  /* Back side */
  .card--back .brand { top: 58px; gap: 16px; }
  .card--back .brand__dot { width: 34px; height: 34px; background: var(--blue-light); }
  .card--back .brand__name { font-size: 21px; color: var(--ink-grey); letter-spacing: 1px; }

  .info-band {
    position: absolute;
    left: 0; right: 0;
    top: 196px;
    height: 290px;
    border-top: 6px solid var(--cyan-line);
    border-bottom: 6px solid var(--cyan-line);
    background: radial-gradient(ellipse at 50% 30%, var(--blue-light) 0%, var(--blue-mid) 45%, var(--blue-deep) 100%);
  }
  .person {
    position: absolute;
    left: 0; right: 0; top: 34px;
    text-align: center;
    font-family: "Open Sans", sans-serif;
    color: var(--white);
  }
  .person__name { font-weight: 700; font-size: 14px; letter-spacing: .3px; }
  .person__role { font-size: 9.5px; letter-spacing: .6px; text-transform: uppercase; margin-top: 2px; }
  .divider {
    position: absolute;
    left: 46px; right: 46px; top: 100px;
    height: 1px;
    background: linear-gradient(to right, transparent, rgba(255,255,255,.9), transparent);
  }
  .contacts {
    position: absolute;
    left: 76px; top: 124px;
    list-style: none;
    font-family: "Open Sans", sans-serif;
    font-size: 11.5px;
    color: var(--white);
  }
  .contacts li { display: flex; align-items: center; gap: 6px; height: 25px; }
  .contacts svg { width: 12px; height: 12px; flex: none; }
  .address {
    position: absolute;
    left: 0; right: 0; top: 486px; bottom: 0;
    display: flex; align-items: center; justify-content: center;
    font-family: "Open Sans", sans-serif;
    font-size: 12px;
    color: var(--address-blue);
  }
</style>
</head>
<body>

<section class="card card--front" aria-label="Card front with clinic name">
  <div class="brand">
    <span class="brand__dot"></span>
    <div class="brand__name">Bright<br>Valley<br>Centre</div>
  </div>
  <div class="tagline-band">Experts in Hearing Care</div>
</section>

<section class="card card--back" aria-label="Card back with contact details">
  <div class="brand">
    <span class="brand__dot"></span>
    <div class="brand__name">Bright<br>Valley<br>Centre</div>
  </div>

  <div class="info-band">
    <div class="person">
      <div class="person__name">YOUR NAME</div>
      <div class="person__role">Designation</div>
    </div>
    <div class="divider"></div>
    <ul class="contacts">
      <li>
        <svg viewBox="0 0 12 12"><rect width="12" height="12" rx="2" fill="#fff"/><path d="M3.4 2.6l1.3 1.5-.7.9c.5 1 1.3 1.9 2.5 2.5l.9-.7 1.5 1.3-.9 1.3C5.8 9.3 2.9 6.4 2.6 3.4z" fill="#2f8ff0"/></svg>
        123-456-7890
      </li>
      <li>
        <svg viewBox="0 0 12 12"><rect width="12" height="12" rx="2" fill="#fff"/><rect x="3" y="2.5" width="6" height="3" fill="#2f8ff0"/><rect x="2" y="5.5" width="8" height="3.5" rx=".6" fill="#2f8ff0"/></svg>
        123-456-7890
      </li>
      <li>
        <svg viewBox="0 0 12 12"><rect width="12" height="12" rx="2" fill="#fff"/><rect x="4" y="2" width="4" height="8" rx=".8" fill="#2f8ff0"/></svg>
        123-456-7890
      </li>
      <li>
        <svg viewBox="0 0 12 12"><rect width="12" height="12" rx="2" fill="#fff"/><rect x="2.2" y="3.3" width="7.6" height="5.4" fill="none" stroke="#2f8ff0" stroke-width="1"/><path d="M2.2 3.3L6 6.3l3.8-3" fill="none" stroke="#2f8ff0" stroke-width="1"/></svg>
        info@yourdomain.com
      </li>
      <li>
        <svg viewBox="0 0 12 12"><rect width="12" height="12" rx="2" fill="#fff"/><circle cx="6" cy="6" r="3.6" fill="none" stroke="#2f8ff0" stroke-width="1"/><path d="M2.4 6h7.2M6 2.4c-1.6 2-1.6 5.2 0 7.2M6 2.4c1.6 2 1.6 5.2 0 7.2" fill="none" stroke="#2f8ff0" stroke-width=".8"/></svg>
        www.yourdomain.com
      </li>
    </ul>
  </div>

  <p class="address">You Office/Shop Address will entered here</p>
</section>

</body>
</html>
```